Training Consultant for Oil and Gas Drillers needs logo for business cards

I teach oil and gas professionals the skills required to keep rigs from blowing up. The company name is "Night Shift Bore Safety", which is pronounced Night Shyft. Tour refers to the time on an oil rig when a worker is off for sleep and rest. I teach something called Well Control, which is how to maintain a pressure balance in the well so the hydro carbons don't come to surface unexpectedly( like the Silver Tide Platform).

Target Market(s)

Rig hands and oil companies

Contact Information for Business Card

Night Shift BS ( company name) with a new logo
My name (Dale Ferrington )and Title (Well Control Consultant)
Phone number and address

Font styles to use
Serif
Sans Serif

Colors

Designer to choose colors to be used in the design.

Requirements
Must have
• I need a logo for the company. I do not have anything yet

```html
<!DOCTYPE html>
<html lang="en">
<head>
<meta charset="utf-8">
<title>Night Shift BS – Business Card</title>
<link rel="stylesheet" href="https://fonts.googleapis.com/css2?family=Arimo:wght@400;700&family=Montserrat:wght@600;800&display=swap">
<style>
  :root {
    --page-bg: #f2f2f2;
    --card-white: #ffffff;
    --panel-navy: #16233b;
    --ink-navy: #1a2540;
    --ink-black: #111111;
    --accent-blue: #2aa3e0;
    --rule-white: #ffffff;
  }
  html, body {
    margin: 0;
    padding: 0;
    width: 1200px;
    height: 1200px;
    overflow: hidden;
    background: var(--page-bg);
  }
  .card {
    position: absolute;
    left: 103px;
    top: 358px;
    width: 1003px;
    height: 574px;
    background: var(--card-white);
    overflow: hidden;
  }
  .identity-panel {
    position: absolute;
    left: 0;
    top: 0;
    width: 503px;
    height: 100%;
    background: var(--panel-navy);
  }
  .person-name {
    position: absolute;
    right: 32px;
    top: 250px;
    margin: 0;
    font-family: "Arimo", Arial, sans-serif;
    font-weight: 700;
    font-size: 36px;
    color: var(--rule-white);
    white-space: nowrap;
  }
  .name-rule {
    position: absolute;
    left: 0;
    top: 296px;
    width: 100%;
    height: 2px;
    background: var(--rule-white);
  }
  .person-title {
    position: absolute;
    right: 32px;
    top: 303px;
    margin: 0;
    font-family: "Arimo", Arial, sans-serif;
    font-weight: 400;
    font-size: 32px;
    color: var(--rule-white);
    white-space: nowrap;
  }
  .brand {
    position: absolute;
    left: 539px;
    top: 26px;
    display: flex;
    flex-direction: column;
    align-items: flex-start;
  }
  .brand-dot {
    width: 52px;
    height: 52px;
    margin-left: 104px;
    border-radius: 50%;
    background: var(--accent-blue);
  }
  .brand-name {
    margin: 14px 0 0;
    font-family: "Montserrat", sans-serif;
    font-weight: 800;
    font-size: 33px;
    letter-spacing: 0.02em;
    color: var(--ink-black);
    white-space: nowrap;
  }
  .contact-list {
    position: absolute;
    left: 539px;
    top: 232px;
    margin: 0;
    padding: 0;
    list-style: none;
    font-family: "Montserrat", sans-serif;
    font-weight: 600;
    font-size: 25px;
    letter-spacing: 0.2em;
    line-height: 45px;
    color: var(--ink-navy);
    white-space: nowrap;
  }
</style>
</head>
<body>
  <div class="card">
    <section class="identity-panel">
      <h1 class="person-name">Dale Ferrington</h1>
      <div class="name-rule"></div>
      <p class="person-title">Well Control Consultant</p>
    </section>

    <div class="brand">
      <div class="brand-dot"></div>
      <p class="brand-name">NIGHT SHIFT BS</p>
    </div>

    <ul class="contact-list">
      <li class="contact-phone">+12 3456 7890 123</li>
      <li class="contact-email">contact@yourbrand</li>
      <li class="contact-web">www.yourbrand</li>
    </ul>
  </div>
</body>
</html>
```